Skin care products for Men Label design

I am looking for a designer, who can help with the label design for my new skin care products line for Men.
Modern design, with a manly feel for ecology products.
Colors that must be included:
Black and Blue (see company logo in uploaded files)

These are the measurements:

Cleanser: MM: 130 x 60

Skintonic : MM:130 x 60

Day Creme: MM 105 x 74

Target Market(s)

Men aged 25-55

Industry/Entity Type

Skin Care Product

Requirements
Must have
• Colors that must be included:

```html
<!DOCTYPE html>
<html lang="en">
<head>
<meta charset="utf-8">
<title>Stone Ridge Face Cleanser Label</title>
<link rel="stylesheet" href="https://fonts.googleapis.com/css2?family=Oswald:wght@300;500&family=Roboto+Condensed:wght@400;700&display=swap">
<style>
  :root {
    --label-black: #0b0b0c;
    --ink-white: #f2f2f2;
    --ink-soft: #d6d6d6;
    --brand-blue: #3b86b8;
    --brand-blue-deep: #1f5f92;
  }
  * { margin: 0; padding: 0; box-sizing: border-box; }
  html, body {
    width: 672px;
    height: 1200px;
    overflow: hidden;
    background: var(--label-black);
  }
  .label {
    position: relative;
    width: 672px;
    height: 1200px;
    background: var(--label-black);
    color: var(--ink-white);
    font-family: "Roboto Condensed", "Arial Narrow", sans-serif;
  }
  .brand {
    position: absolute;
    top: 250px;
    left: 0;
    width: 100%;
    display: flex;
    justify-content: center;
    align-items: center;
    gap: 18px;
  }
  .brand-square {
    width: 46px;
    height: 46px;
    background: var(--brand-blue-deep);
  }
  .brand-name {
    font-family: "Roboto Condensed", "Arial Narrow", sans-serif;
    font-weight: 700;
    font-size: 46px;
    color: var(--ink-white);
    letter-spacing: 0.5px;
  }
  .product-title {
    position: absolute;
    top: 430px;
    left: 0;
    width: 100%;
    text-align: center;
    font-family: "Oswald", "Arial Narrow", sans-serif;
    line-height: 1;
  }
  .product-kind {
    display: block;
    font-weight: 300;
    font-size: 104px;
    color: var(--ink-soft);
    letter-spacing: 2px;
  }
  .product-name {
    display: block;
    margin-top: 18px;
    font-weight: 500;
    font-size: 120px;
    color: var(--ink-white);
    letter-spacing: 1px;
  }
  .audience-band {
    position: absolute;
    top: 780px;
    left: 88px;
    width: 100px;
    height: 370px;
    background: var(--brand-blue);
    display: flex;
    align-items: center;
    justify-content: center;
  }
  .audience-text {
    transform: rotate(-90deg);
    white-space: nowrap;
    font-family: "Oswald", "Arial Narrow", sans-serif;
    font-weight: 500;
    font-size: 50px;
    color: var(--ink-white);
    letter-spacing: 2px;
  }
  .benefits {
    position: absolute;
    top: 790px;
    left: 222px;
    font-size: 38px;
    line-height: 1.4;
  }
  .benefit-main { color: var(--ink-soft); font-weight: 400; }
  .benefit-detail { color: var(--ink-white); font-weight: 400; }
  .volume {
    position: absolute;
    top: 1060px;
    left: 222px;
    font-size: 34px;
    color: var(--ink-soft);
    letter-spacing: 0.5px;
  }
</style>
</head>
<body>
  <main class="label">
    <div class="brand">
      <span class="brand-square" aria-hidden="true"></span>
      <span class="brand-name">Stone Ridge</span>
    </div>
    <h1 class="product-title">
      <span class="product-kind">FACE</span>
      <span class="product-name">CLEANSER</span>
    </h1>
    <div class="audience-band">
      <span class="audience-text">FOR MEN</span>
    </div>
    <div class="benefits">
      <p class="benefit-main">MOISTURIZING</p>
      <p class="benefit-detail">WITH ALOE &amp; TEA TREE</p>
    </div>
    <p class="volume">16 FL OZ (473 ML)</p>
  </main>
</body>
</html>
```